Velora Harvest Company product labels (5"wide x7" high (12,5 cm x 17,5 cm))

We need a vertical product label that will go on the Gold stand up bags for our Kratom powder. We are looking for professional looking and attractive label design that will capture the attention of consumers. Our products should stand out when sitting on a shelf next to our competitors. We want one label which we will be able to use for all the different Kratom Powders we have.The product label will be used for several different varieties of Kratom so there will need to be an area available for the varieties name such as "RED BORNEO" or "GREEN MAENG DA" etc., which we will apply a small label as needed.
The label dimensions should be 5" wide x 7" high (12,5 cm wide x 17,5 cm high).
Please review the "must haves" section, and please try and include the "nice to haves" if possible.

Target Market(s)

Health minded consumers who love natural products, and are looking for plant based alternatives to harmful synthetic products.

Industry/Entity Type

Supplement

Colors

Designer to choose colors to be used in the design.

Requirements
Must have
• Product labels must include:
• 1) Company logo (find in the attachments)
• 2) Product information (find in the attachments)
• 3) Product title - Premium Kratom Powder
• 4) Weight indication - 250 grams
• 5) Barcode
• 6) Icon that says - 100% pure (or "100% natural")
Nice to have
• Indonesian jungle theme.
• Our packaging is gold metallic stand up bag, so the colors should be complimenting the bag.
Should not have
• labels or part of the labels taken from other Kratom companies. The design should be unique.

```html
<!DOCTYPE html>
<html lang="en">
<head>
<meta charset="utf-8">
<title>Velora Harvest Company – Premium Kratom Powder Labels</title>
<link href="https://fonts.googleapis.com/css2?family=Fredoka:wght@600&family=Quicksand:wght@500;700&family=Patrick+Hand&display=swap" rel="stylesheet">
<style>
  :root {
    --backdrop: #e9e6dc;
    --label-light: #f3f0c4;
    --label-mid: #e2e39a;
    --label-edge: #c9d67a;
    --forest: #2f3d1a;
    --leaf: #5c7a22;
    --leaf-soft: #8fb04a;
    --cream: #fbf6dc;
    --text-dark: #2b2a17;
    --flower: #f2a26a;
  }
  html, body {
    margin: 0;
    width: 1200px;
    height: 823px;
    overflow: hidden;
    background: var(--backdrop);
  }
  .canvas {
    position: relative;
    width: 1200px;
    height: 823px;
  }
  .label {
    position: absolute;
    top: 62px;
    width: 500px;
    height: 700px;
    overflow: hidden;
    background: radial-gradient(ellipse at 50% 55%, var(--label-light) 0%, var(--label-mid) 70%, var(--label-edge) 100%);
    box-shadow: 0 6px 24px rgba(40, 45, 20, 0.18);
  }
  .label--front { left: 70px; }
  .label--back { left: 630px; }

  .foliage {
    position: absolute;
    border-radius: 50%;
    opacity: 0.85;
  }
  .foliage--top-left {
    left: -90px; top: -80px; width: 260px; height: 360px;
    background: radial-gradient(circle at 60% 55%, var(--leaf-soft) 0%, rgba(143,176,74,0.55) 45%, rgba(143,176,74,0) 72%);
  }
  .foliage--top-right {
    right: -90px; top: -80px; width: 260px; height: 360px;
    background: radial-gradient(circle at 40% 55%, var(--leaf-soft) 0%, rgba(143,176,74,0.55) 45%, rgba(143,176,74,0) 72%);
  }
  .foliage--bottom-left {
    left: -80px; bottom: -90px; width: 260px; height: 280px;
    background: radial-gradient(circle at 55% 45%, var(--leaf) 0%, rgba(92,122,34,0.5) 45%, rgba(92,122,34,0) 72%);
  }
  .foliage--bottom-right {
    right: -80px; bottom: -90px; width: 260px; height: 280px;
    background: radial-gradient(circle at 45% 45%, var(--flower) 0%, rgba(92,122,34,0.55) 40%, rgba(92,122,34,0) 72%);
  }

  .banner {
    position: absolute;
    left: 50%;
    top: 0;
    width: 224px;
    height: 278px;
    margin-left: -112px;
    background: var(--forest);
    clip-path: polygon(0 0, 100% 0, 100% 100%, 50% 91%, 0 100%);
  }
  .label--back .banner { height: 268px; }
  .brand {
    position: absolute;
    left: 50%;
    top: 72px;
    width: 160px;
    height: 160px;
    margin-left: -80px;
    border: 3px solid var(--cream);
    border-radius: 50%;
    box-sizing: border-box;
    display: flex;
    align-items: center;
    justify-content: center;
    text-align: center;
  }
  .label--back .brand { top: 66px; }
  .brand__name {
    font-family: "Quicksand", sans-serif;
    font-weight: 700;
    color: var(--cream);
    font-size: 21px;
    line-height: 1.15;
    letter-spacing: 1px;
    text-transform: uppercase;
  }

  .title {
    position: absolute;
    left: 0;
    width: 100%;
    top: 302px;
    text-align: center;
    margin: 0;
  }
  .title__main {
    display: block;
    font-family: "Fredoka", sans-serif;
    font-weight: 600;
    font-size: 86px;
    line-height: 1;
    color: var(--forest);
    letter-spacing: 1px;
  }
  .title__sub {
    display: block;
    margin-top: 4px;
    font-family: "Quicksand", sans-serif;
    font-weight: 700;
    font-size: 33px;
    line-height: 1.1;
    color: var(--leaf);
  }

  .weight-panel {
    position: absolute;
    left: 50%;
    bottom: 0;
    width: 210px;
    height: 238px;
    margin-left: -105px;
    background: var(--forest);
    clip-path: polygon(0 0, 50% 6%, 100% 0, 100% 100%, 0 100%);
  }
  .claim {
    position: absolute;
    left: 50%;
    bottom: 96px;
    width: 170px;
    margin-left: -85px;
    text-align: center;
    font-family: "Patrick Hand", cursive;
    color: var(--cream);
  }
  .claim__percent {
    display: block;
    font-size: 42px;
    line-height: 1;
  }
  .claim__word {
    display: inline-block;
    margin-top: 6px;
    padding: 2px 14px 4px;
    background: var(--leaf);
    border-radius: 6px;
    font-size: 40px;
    line-height: 1;
  }
  .net-weight {
    position: absolute;
    left: 0;
    width: 100%;
    bottom: 36px;
    margin: 0;
    text-align: center;
    font-family: "Quicksand", sans-serif;
    font-weight: 700;
    font-size: 19px;
    color: var(--cream);
  }

  .info {
    position: absolute;
    left: 30px;
    right: 30px;
    top: 296px;
    text-align: center;
    font-family: "Quicksand", sans-serif;
    color: var(--text-dark);
  }
  .info p { margin: 0; }
  .info__ingredients { font-weight: 700; font-size: 15px; line-height: 1.35; }
  .info__warning {
    margin-top: 26px !important;
    font-weight: 700;
    font-size: 14px;
    line-height: 1.35;
    text-transform: uppercase;
  }
  .info__disclaimer {
    margin: 18px auto 0 !important;
    width: 330px;
    font-weight: 500;
    font-size: 10.5px;
    line-height: 1.45;
  }
  .info__distributor {
    margin-top: 22px !important;
    font-weight: 700;
    font-size: 13px;
    line-height: 1.4;
  }
  .barcode-area {
    position: absolute;
    left: 50%;
    top: 604px;
    width: 220px;
    height: 50px;
    margin-left: -110px;
    background: var(--forest);
    display: flex;
    align-items: center;
    justify-content: center;
    font-family: "Quicksand", sans-serif;
    font-weight: 700;
    font-size: 13px;
    color: var(--cream);
  }
</style>
</head>
<body>
<main class="canvas">

  <section class="label label--front" aria-label="Front label">
    <div class="foliage foliage--top-left" role="img" aria-label="Tropical palm leaves and pink frangipani illustration"></div>
    <div class="foliage foliage--top-right" role="img" aria-label="Tropical leaves and yellow frangipani illustration"></div>
    <div class="foliage foliage--bottom-left" role="img" aria-label="Jungle fern and palm leaf illustration"></div>
    <div class="foliage foliage--bottom-right" role="img" aria-label="Orange hibiscus and bird of paradise flower illustration"></div>

    <div class="banner"></div>
    <div class="brand">
      <span class="brand__name">Velora<br>Harvest<br>Company</span>
    </div>

    <h1 class="title">
      <span class="title__main">PREMIUM</span>
      <span class="title__sub">KRATOM POWDER</span>
    </h1>

    <div class="weight-panel"></div>
    <div class="claim">
      <span class="claim__percent">100%</span>
      <span class="claim__word">natural</span>
    </div>
    <p class="net-weight">250 grams</p>
  </section>

  <section class="label label--back" aria-label="Back label">
    <div class="foliage foliage--top-left" role="img" aria-label="Tropical palm leaves illustration"></div>
    <div class="foliage foliage--top-right" role="img" aria-label="Tropical leaves and yellow frangipani illustration"></div>
    <div class="foliage foliage--bottom-left" role="img" aria-label="Jungle fern and palm leaf illustration"></div>
    <div class="foliage foliage--bottom-right" role="img" aria-label="Orange hibiscus flower illustration"></div>

    <div class="banner"></div>
    <div class="brand">
      <span class="brand__name">Velora<br>Harvest<br>Company</span>
    </div>

    <div class="info">
      <p class="info__ingredients">INGREDIENTS:<br>100% natural Mitragyna Speciosa leaf powder.</p>
      <p class="info__warning">Not for sale to minors.<br>Must be 18 years or older to purchase.<br>Keep out of reach of children.</p>
      <p class="info__disclaimer">Do not use any botanicals without a physician's consent, if you are a minor, pregnant, nursing or taking MAOIs. These statements have not been evaluated by the FDA and is not intended to diagnose, treat, cure or prevent any disease. Caution while driving or using heavy machinery.</p>
      <p class="info__distributor">Distributed by:<br>VELORA HARVEST COMPANY MARLOW BEND,<br>FL 32001</p>
    </div>

    <div class="barcode-area">BAR CODE</div>
  </section>

</main>
</body>
</html>
```